Wordpress Design Project - Wedding Magazine Website

After looking at a few similar websites I formed a layout and colour scheme design in my head.
Then I came across this site (www.petalmarch.co.uk) which very close to what I am looking for in terms of layout of the page content and colours. So I would like something very similar but not so similar it just looks like a clone of this site. Almost identical in terms of how the content is laid out but colours and look and feel can be changed.
I have also provided a sketch of how I would like the content of the page to flow. See attachment.
Similar websites: in terms of content, style and layout.
http://www.lacebellmag.com/ (the colour scheme is good on this site. I also would like a similar background image as they have on their site.)
http://www.nuptivox.com/ (style and colour scheme is good on this site.)
of course you have the other sites i have reference in the initial tender.
Other general examples of wedding magazine style websites.
http://www.vowbrook.co.uk/
http://www.ringsandgarlands.co.uk/
http://www.thegoldenaisle.com/
http://www.veilor.com/
Style and layout: Wedding Theme
Colour Scheme: Clean and simple. White background in content area. Hints or highlights of grey/sliver, maybe pink here and there.
The page will flow as follows
Header part of the Page
- Name of the site on top left part of the page. “Tied by the Sea”.
- 728x90 horizontal banner aligned on right.
- Under the site name “Tied by the Sea” and banner will be a horizontal menu bar running the full width of the content
Main Content Area
- The main content column will be about 630px and the right sidebar will be about 330px. Similar width to most of the example URLs I have provided.
- Aligned to the left will be a slider
- Graphic or Pic: Guide to marrying in Spain: Everything you need to plan your wedding in spain.
- Graphic: Local Vendors Directory
- Articles 1 – 4
Right Sidebar (About 330px):
- Popular Post: Title of the Post and the first 2-3 lines of the post.
- 300x250 Ad Slot
- Locations: Title such as Barcelona then the first 2-3 lines of the post.
note: I haven't included a search box and login/register bits of content. i will leave it to you to figure out where these things will fit best on the page
=========================================================
Content of page
The horizontal menu bar: Home, Spanish Wedding Guide, Local Vendors Directory, Venues, Stag & Hen, Planning, Deals, Wedding Store.
For the wordpress theme the horizontal menubar will need to be a drop down menubar as we will have sub-menus for some of pages.
Images for slider
- Featured Venues
- Local vendors
- Deals
THE 2 COLUMN CONTENT AREA (Articles/Posts)
I am thinking that the first two bits of content in the 2 column area maybe should be graphics.
Spanish Wedding Guide -
Everything you need to plan your wedding in Spain.
Local Vendors Directory
(maybe this could be a graphic of a map of Spain)
=== from here you could use pictures or a mix of graphics and pictures to accompany each of these articles===
Front Page Main Content Articles
1. Legalities -
Want to tie the knot in Spain then you will find this post very useful.
2. Destination Barcelona -
Everything We LOVE About Barcelona!
3. Celebrity Weddings in Spain -
Find out who the latest celebrities to get married and Spain are and their chosen location.
4. Beach Weddings - With 4,964 km of coastline in Spain it is no surprise beach weddings are a popular choice.
under this will be the footer
Content we can populate later.
http://www.vowbrook.co.uk/
http://www.veilor.com/
Header part of the Page
- Under the site name “Tied by the Sea” will be a horizontal menu bar running the full width of the content
Main Content Area
- The main content column will be about 630px and the right sidebar will be about 330px. Similar width to most of the
example URLs I have provided.
Graphic or Pic: Guide to marrying in Spain: Everything you need to plan your wedding in spain.
Article 1 – 4
- 300x250 Ad Slot
note: i have left out a search bar and login area. I will leave that up to you. where you think they will fit on the page.
Content of page
Images for slider
- Featured Venues
- Local vendors
- Deals
Spanish Wedding Guide -
Local Vendors Directory
1. Legalities -
Please contact me for any questions. it maybe better to speak via skype or something.
Project Deadline Extended
Reason: It took me a few days to get acquainted with this site. As I don't have any designs in just yet I am extending the project a few days in order to give people time to submit their designs.
Something I would like to ad that i think designers will find useful.
The core of this site is the “Spanish Wedding Guide” and the “Local Vendor Directory”. These two things are what the site is all about so they need to feature. The viewers eyes must be drawn immediately to these two bit of information upon loading the page. These two things go underneath the slider.

```html
<!DOCTYPE html>
<html lang="en">
<head>
<meta charset="utf-8">
<title>Tied by the Sea</title>
<link href="https://fonts.googleapis.com/css2?family=PT+Sans:wght@400;700&family=Roboto:wght@400;700&display=swap" rel="stylesheet">
<style>
:root{
  --pink:#e2177c;
  --pink-light:#f04a9b;
  --pink-deep:#a8195e;
  --page-bg:#fbe4ee;
  --panel:#f2f2f2;
  --panel-line:#dcdcdc;
  --text:#444;
  --muted:#777;
  --btn:#4a4a4a;
  --sand:#e3ceaa;
  --white:#fff;
}
*{margin:0;padding:0;box-sizing:border-box}
html,body{width:960px;height:1200px;overflow:hidden}
body{background:var(--page-bg);font-family:"Roboto",Arial,sans-serif;color:var(--text);position:relative}
.abs{position:absolute}
.page{position:absolute;left:82px;top:0;width:796px;height:1200px;background:var(--white)}
.head-font{font-family:"PT Sans",Arial,sans-serif}

/* header */
.logo{left:112px;top:36px;font-family:"PT Sans",Arial,sans-serif;font-weight:700;font-size:27px;color:var(--pink)}
.banner{left:354px;top:17px;width:516px;height:72px;border:1px solid #555;background:var(--white)}
.banner-art{left:4px;top:4px;width:117px;height:62px;background:linear-gradient(180deg,#d9c19a,#c9a98a);}
.banner-main{left:4px;top:4px;width:378px;height:62px;background:var(--sand)}
.banner-cta{left:190px;top:14px;font-family:"PT Sans",sans-serif;font-size:17px;line-height:21px;color:#7a6a55;text-align:center}
.banner-brand{right:12px;top:12px;text-align:right;font-family:"PT Sans",sans-serif;color:#666;font-size:25px;line-height:26px}
.banner-brand small{display:block;font-size:12px;line-height:16px}

/* nav */
.nav{left:82px;top:105px;width:796px;height:31px;background:var(--pink);display:flex}
.nav a{font-family:"PT Sans",sans-serif;font-weight:700;color:var(--white);font-size:12px;text-decoration:none;line-height:31px;text-align:center;border-right:1px solid rgba(255,255,255,.25)}
.nav a:last-child{border-right:0}

/* slider */
.slider{left:87px;top:154px;width:516px;height:213px;border:3px solid #ddd;background:var(--white);padding:2px}
.slider .ph{width:100%;height:100%;background:linear-gradient(90deg,#6b5248,#c9a79a 50%,#e9d9d6)}

/* section headings */
.sec-title{font-family:"PT Sans",sans-serif;font-size:17px;color:#666}
.sec-title b{color:var(--pink)}
.guide-list{left:98px;top:419px;list-style:none;font-size:10px;letter-spacing:.3px}
.guide-list li{height:20.8px;padding-left:11px;position:relative}
.guide-list li::before{content:"";position:absolute;left:0;top:3px;border-left:4px solid var(--pink);border-top:3px solid transparent;border-bottom:3px solid transparent}
.map{left:356px;top:416px;width:243px;height:156px;border:1px solid #ccc;border-radius:3px;padding:4px;background:var(--white)}
.map .ph{width:100%;height:100%;background:linear-gradient(135deg,#9fd3ec,#a5c96e 45%,#cdd88a 70%,#8ccbe8)}

.btn{height:16px;border-radius:8px;background:var(--btn);color:var(--white);font-size:9.5px;letter-spacing:.5px;text-align:center;line-height:16px}

/* article bars */
.bar{height:23px;border-radius:11px;background:linear-gradient(180deg,var(--pink-light),var(--pink));color:var(--white);font-family:"PT Sans",sans-serif;font-weight:700;font-size:13px;line-height:23px;padding-left:12px}
.thumb{width:96px;height:112px;border:1px solid #ddd;padding:5px;background:var(--white)}
.thumb .ph{width:100%;height:100%}
.art-title{font-size:11px;font-weight:700;color:var(--pink);letter-spacing:.5px}
.art-text{font-size:9.5px;line-height:14.4px;letter-spacing:.4px;color:#444}

/* sidebar */
.panel{background:var(--panel);border:1px solid var(--panel-line)}
.post{left:14px;width:220px}
.post .sq{position:absolute;left:0;top:4px;width:11px;height:9px}
.post h4{margin-left:20px;font-weight:400;font-size:10.5px;color:var(--pink)}
.post p{margin-left:20px;margin-top:3px;font-size:9.5px;line-height:14.4px;letter-spacing:.4px;color:#555}
.post .more{position:absolute;right:0;font-size:9px;color:var(--pink);border-bottom:1px solid var(--pink);padding-right:8px}
.post .more::after{content:"";position:absolute;right:1px;top:3px;border-left:3px solid var(--pink);border-top:2.5px solid transparent;border-bottom:2.5px solid transparent}
.divider{left:12px;width:224px;border-top:1px dashed #bbb}
.ad{left:631px;top:456px;width:240px;height:199px;border:1px solid #333;background:var(--white)}
.ad-fill{left:4px;top:4px;width:230px;height:144px;background:var(--sand)}
.ad-cta{left:0;width:100%;top:54px;text-align:center;font-family:"PT Sans",sans-serif;color:#7a6a55;font-size:14px;line-height:18px}
.ad-brand{right:18px;top:156px;text-align:right;font-family:"PT Sans",sans-serif;color:#666;font-size:19px;line-height:20px}
.ad-brand small{display:block;font-size:10px;line-height:13px}
.loc{left:72px;font-size:9.5px;line-height:19.2px;letter-spacing:.3px;color:#555}
.loc b{color:#333}
.pin{left:18px;width:44px;height:44px}

/* footer */
.footer{left:82px;top:988px;width:796px;height:183px;background:linear-gradient(180deg,#f33a99,#e02685 45%,#a61a62)}
.footer-strip{left:82px;top:1165px;width:796px;height:6px;background:#f05aa6}
.f-title{font-family:Arial,sans-serif;font-weight:700;font-size:11px;color:var(--white);border-bottom:1px dashed rgba(255,255,255,.6);padding-bottom:2px}
.f-links{list-style:none;font-family:Arial,sans-serif;font-size:9.5px;line-height:15.2px;color:#ffd0e8}
.quote{font-family:Arial,sans-serif;font-weight:700;font-size:10px;line-height:14.4px;letter-spacing:.6px;color:var(--white)}
.contact{font-family:Arial,sans-serif;font-size:9.5px;line-height:13.6px;color:#ffd0e8}
.contact b{color:var(--white)}
.copy{left:109px;top:1184px;font-family:Arial,sans-serif;font-size:8px;color:#777}
</style>
</head>
<body>
<div class="page"></div>

<!-- header -->
<div class="abs logo">Tied by the Sea</div>
<div class="abs banner">
  <div class="abs banner-main"></div>
  <div class="abs banner-art" role="img" aria-label="Illustration of a wedding gift shelf with presents"></div>
  <div class="abs banner-cta">› Create your<br>Gift List</div>
  <div class="abs banner-brand">Marlow Hart<small>marlowhart.com</small></div>
</div>

<nav class="abs nav">
  <a style="width:60px">Home</a>
  <a style="width:155px">Spanish Wedding Guide</a>
  <a style="width:156px">Local Vendors Directory</a>
  <a style="width:77px">Venues</a>
  <a style="width:96px">Stag &amp; Hen</a>
  <a style="width:81px">Planning</a>
  <a style="width:68px">Deals</a>
  <a style="width:103px">Wedding Store</a>
</nav>

<!-- slider -->
<div class="abs slider"><div class="ph" role="img" aria-label="Photo of a bride and groom touching foreheads"></div></div>

<!-- guide & directory -->
<div class="abs sec-title" style="left:100px;top:387px">Spanish Wedding <b>Guide</b></div>
<ul class="abs guide-list">
  <li>Treat your guests with our wedding favours.</li>
  <li>Contemporary and traditional wedding stationery.</li>
  <li>Stunning jewellery for brides, bridesmaids and .</li>
  <li>Make it personal with our huge range of gifts.</li>
  <li>Choose from our wide range of wedding gift ideas.</li>
  <li>Make it personal with our huge range of gifts.</li>
  <li>Choose from our wide range of wedding gift ideas.</li>
  <li>Browse our fun selection.</li>
</ul>
<div class="abs sec-title" style="left:360px;top:387px">Local Vendors <b>Directory</b></div>
<div class="abs map"><div class="ph" role="img" aria-label="Map of Spain and Portugal"></div></div>
<div class="abs btn" style="left:532px;top:584px;width:66px">Read More</div>

<!-- articles row 1 -->
<div class="abs bar" style="left:86px;top:612px;width:253px">Legalities</div>
<div class="abs bar" style="left:357px;top:612px;width:253px">Destination Barcelona</div>

<div class="abs thumb" style="left:88px;top:652px"><div class="ph" role="img" aria-label="Photo of a bride and groom cutting the wedding cake" style="background:linear-gradient(135deg,#e9dccb,#b69a80)"></div></div>
<div class="abs art-title" style="left:193px;top:653px">Legalities</div>
<div class="abs art-text" style="left:193px;top:667px;width:133px;text-align:justify">Want to tie the knot in Spain then you will find this post very useful.</div>
<div class="abs btn" style="left:258px;top:751px;width:66px">Read More</div>

<div class="abs thumb" style="left:363px;top:654px"><div class="ph" role="img" aria-label="Photo of a bride in a church aisle" style="background:linear-gradient(180deg,#3c2a22,#8a6a58 60%,#d9d2cc)"></div></div>
<div class="abs art-title" style="left:466px;top:655px">Destination Barcelona</div>
<div class="abs art-text" style="left:466px;top:669px;width:133px;text-align:justify">Everything We LOVE About Barcelona!</div>
<div class="abs btn" style="left:535px;top:751px;width:66px">Read More</div>

<!-- articles row 2 -->
<div class="abs bar" style="left:86px;top:800px;width:253px;padding-left:16px">Celebrity Weddings in Spain</div>
<div class="abs bar" style="left:357px;top:800px;width:253px">Beach Weddings</div>

<div class="abs thumb" style="left:88px;top:840px"><div class="ph" role="img" aria-label="Photo of a bride signing the wedding register" style="background:linear-gradient(135deg,#d9cfc6,#6e5648)"></div></div>
<div class="abs art-title" style="left:191px;top:849px;font-size:10px;letter-spacing:0">Celebrity Weddings in Spain</div>
<div class="abs art-text" style="left:191px;top:863px;width:143px;text-align:justify">Find out who the latest celebri-ties to get married and Spain are and their chosen location.</div>
<div class="abs" style="left:191px;top:922px;font-size:9.5px;color:var(--pink);letter-spacing:.4px">Read More &gt;</div>
<div class="abs btn" style="left:282px;top:934px;width:67px">Read More</div>

<div class="abs thumb" style="left:365px;top:841px"><div class="ph" role="img" aria-label="Photo of a couple on a beach" style="background:linear-gradient(180deg,#a9d8ee,#6fb9d6 55%,#efe6d8)"></div></div>
<div class="abs art-title" style="left:466px;top:842px">Beach Weddings</div>
<div class="abs art-text" style="left:466px;top:856px;width:133px;text-align:justify">With 4,964 km of coastline in Spain it is no surprise beach weddings are a popular choice.</div>
<div class="abs btn" style="left:535px;top:934px;width:66px">Read More</div>

<!-- sidebar: latest posts -->
<div class="abs panel" style="left:622px;top:144px;width:249px;height:295px">
  <div class="abs sec-title" style="left:10px;top:10px;font-size:16px"><span style="color:#777">LATEST </span><b>POSTS</b></div>
  <div class="abs post" style="top:46px">
    <svg class="sq" viewBox="0 0 11 9"><rect x="0" y="4" width="5" height="5" fill="#999"/><rect x="6" y="0" width="5" height="4" fill="#bbb"/><rect x="6" y="5" width="5" height="4" fill="#999"/></svg>
    <h4>Marry in a Hurry!</h4>
    <p>Lorem Ipsum is simply dummy text of the printing and typesetting industry. Lorem Ipsum has been</p>
    <span class="more" style="top:66px">Read more</span>
  </div>
  <div class="abs divider" style="top:122px"></div>
  <div class="abs post" style="top:127px">
    <svg class="sq" viewBox="0 0 11 9"><rect x="0" y="4" width="5" height="5" fill="#999"/><rect x="6" y="0" width="5" height="4" fill="#bbb"/><rect x="6" y="5" width="5" height="4" fill="#999"/></svg>
    <h4>Proposing on Feb 29th?</h4>
    <p>Lorem Ipsum is simply dummy text of the printing and typesetting industry. Lorem Ipsum has been</p>
    <span class="more" style="top:62px">Read more</span>
  </div>
  <div class="abs divider" style="top:204px"></div>
  <div class="abs post" style="top:209px">
    <svg class="sq" viewBox="0 0 11 9"><rect x="0" y="4" width="5" height="5" fill="#999"/><rect x="6" y="0" width="5" height="4" fill="#bbb"/><rect x="6" y="5" width="5" height="4" fill="#999"/></svg>
    <h4>Up to 65% Off</h4>
    <p>Lorem Ipsum is simply dummy text of the printing and typesetting industry. Lorem Ipsum has been</p>
    <span class="more" style="top:70px">Read more</span>
  </div>
</div>

<!-- sidebar: ad -->
<div class="abs ad">
  <div class="abs ad-fill"></div>
  <div class="abs ad-cta">› Create your<br>Gift List</div>
  <div class="abs ad-brand">Marlow Hart<small>marlowhart.com</small></div>
</div>

<!-- sidebar: locations -->
<div class="abs panel" style="left:622px;top:669px;width:249px;height:295px">
  <div class="abs sec-title" style="left:9px;top:12px;font-size:16px"><span style="color:#777">Our </span><b>LOCATIONS</b></div>
  <svg class="abs pin" style="top:52px" viewBox="0 0 44 44"><ellipse cx="28" cy="34" rx="12" ry="4" fill="#ccc"/><path d="M8 10 L22 6 L26 20 L12 24 Z" fill="#f7c21e"/><rect x="10" y="18" width="18" height="8" rx="3" transform="rotate(-15 19 22)" fill="#e8a412"/><path d="M20 25 L30 35" stroke="#999" stroke-width="2"/></svg>
  <div class="abs loc" style="top:50px"><b>Toll Free (spain):</b> 1-866-555-0142<br><b>Toll Free (spain):</b> 1-800-555-017<br><b>Phone:</b> 416-555-0193</div>
  <svg class="abs pin" style="top:136px" viewBox="0 0 44 44"><ellipse cx="28" cy="34" rx="12" ry="4" fill="#ccc"/><path d="M8 10 L22 6 L26 20 L12 24 Z" fill="#f7c21e"/><rect x="10" y="18" width="18" height="8" rx="3" transform="rotate(-15 19 22)" fill="#e8a412"/><path d="M20 25 L30 35" stroke="#999" stroke-width="2"/></svg>
  <div class="abs loc" style="top:134px"><b>Toll Free (spain):</b> 1-866-555-0142<br><b>Toll Free (spain):</b> 1-800-555-017<br><b>Phone:</b> 416-555-0193</div>
  <svg class="abs pin" style="top:228px" viewBox="0 0 44 44"><ellipse cx="28" cy="34" rx="12" ry="4" fill="#ccc"/><path d="M8 10 L22 6 L26 20 L12 24 Z" fill="#f7c21e"/><rect x="10" y="18" width="18" height="8" rx="3" transform="rotate(-15 19 22)" fill="#e8a412"/><path d="M20 25 L30 35" stroke="#999" stroke-width="2"/></svg>
  <div class="abs loc" style="top:226px"><b>Toll Free (spain):</b> 1-866-555-0142<br><b>Toll Free (spain):</b> 1-800-555-017<br><b>Phone:</b> 416-555-0193</div>
</div>

<!-- footer -->
<div class="abs" style="left:82px;top:984px;width:796px;border-top:1px dashed #aaa"></div>
<div class="abs footer"></div>
<div class="abs footer-strip"></div>

<div class="abs f-title" style="left:107px;top:1012px;width:123px">LINKS</div>
<ul class="abs f-links" style="left:108px;top:1043px">
  <li>Home</li><li>About Us</li><li>Contact Us</li><li>Store</li><li>My Accounts</li><li>View Cart</li>
</ul>

<div class="abs f-title" style="left:305px;top:1012px;width:276px">TESTIMONIALS</div>
<div class="abs" style="left:304px;top:1040px;font-family:Georgia,serif;font-size:36px;line-height:36px;color:#f7a6cf">“</div>
<div class="abs quote" style="left:334px;top:1045px;width:222px">Lorem Ipsum is simply dummy text of the printing and typesetting industry. Lorem Ipsum has been orem Ipsum has been</div>
<div class="abs" style="left:333px;top:1098px;font-family:'PT Sans',sans-serif;font-size:8.5px;color:#ffd0e8">Maren Holt, CEO, Company name</div>

<div class="abs f-title" style="left:648px;top:1012px;width:214px">CONTACT DETAILS</div>
<div class="abs contact" style="left:648px;top:1042px;width:230px"><b>Linden Loom</b><br>Lorem ipsum dolor sit amet, etuer adipiscing</div>
<div class="abs contact" style="left:649px;top:1076px"><b>Phone:</b> 555 0100 0199</div>
<div class="abs contact" style="left:649px;top:1094px"><b>Email:</b> admin@tiedbythesea.com</div>

<div class="abs copy">Copyright ©2011-12 by <span style="font-size:9px;color:#555">Tied by the Sea</span> &nbsp;&nbsp;&nbsp;&nbsp; All Rights Reserved. &nbsp;Privact &nbsp;| &nbsp;Terms and Conditions</div>
</body>
</html>
```